Bay & Meadow Property Services Tri-fold sales & marketing brochure

We need a tri-fold brochure that describes our three lines of business and the various services within each line to use in sales and marketing efforts.
See website for additional background info:
https://halvernq7.example-host.com/

Target Market(s)

Real Estate Investors & owners in Residential Rental, Short-term Rentals, and Mini/Maxi Storage Rental markets

Requirements
Must have
• See attached logo, use color scheme & font styles to match. Make sure to utilize photos to enhance look/feel.

```html
<!DOCTYPE html>
<html lang="en">
<head>
<meta charset="utf-8">
<title>Bay &amp; Meadow Property Services – Tri-fold Brochure</title>
<link href="https://fonts.googleapis.com/css2?family=Poppins:wght@400;500;600;700;800&family=Great+Vibes&family=Libre+Baskerville&display=swap" rel="stylesheet">
<style>
:root{
  --blue:#09a3cb;
  --ink:#231f20;
  --white:#ffffff;
  --page:#f1f1f1;
  --text:#2a2a2a;
}
*{box-sizing:border-box;margin:0;padding:0}
html,body{width:758px;height:1200px;overflow:hidden;background:var(--page)}
body{position:relative;font-family:"Poppins",sans-serif;color:var(--text)}
.sheet{position:absolute;left:60px;width:638px;height:493px;background:var(--white);box-shadow:0 2px 8px rgba(0,0,0,.18);overflow:hidden}
.sheet-outside{top:80px}
.sheet-inside{top:628px}
.panel{position:absolute;top:0;height:100%;width:213px}
.abs{position:absolute}
.blue{color:var(--blue)}
.h-title{font-weight:700;font-size:12px;line-height:11.5px;color:var(--ink)}
.h-title .blue{display:block}
.body-copy{font-size:6.1px;line-height:7.8px}
.dots{display:flex;gap:5px;justify-content:center}
.dots i{width:3px;height:3px;border-radius:50%;background:currentColor;display:block}

/* service items */
.item{position:absolute;width:190px;height:36px}
.item-icon{position:absolute;left:0;top:-3px;width:18px;height:18px;border-radius:50%;background:var(--blue);border:1px solid var(--white);display:flex;align-items:center;justify-content:center;z-index:2}
.item-icon.dark{background:var(--ink)}
.item-icon svg{width:10px;height:10px}
.item-pill{position:absolute;left:16px;top:0;width:113px;height:12px;border-radius:6px;padding-left:6px;font-size:7px;font-weight:700;line-height:12px}
.pill-dark{background:var(--ink);color:var(--white)}
.pill-blue{background:var(--blue);color:var(--white)}
.pill-light{background:var(--white);color:var(--ink)}
.item-desc{position:absolute;left:23px;top:16px;width:150px;font-size:6.1px;line-height:7.5px}
.on-dark .item-desc{color:var(--white)}

/* why list */
.why{position:absolute;left:25px;width:170px}
.why-title{font-size:8px;font-weight:700;color:var(--blue);line-height:9px;display:flex;align-items:center;gap:3px}
.why-title svg{width:7px;height:7px}
.why-desc{padding-left:9px;font-size:6.1px;line-height:7.6px;color:var(--white)}

/* brand */
.brand{display:flex;align-items:center;gap:5px}
.brand-dot{width:20px;height:20px;border-radius:50%;background:var(--blue);flex:none}
.brand-name{font-weight:600;font-size:8.5px;line-height:10px;letter-spacing:.4px}

.photo{position:absolute;overflow:hidden}
.photo-circle{border-radius:50%}
</style>
</head>
<body>

<!-- OUTSIDE SHEET -->
<section class="sheet sheet-outside">

  <!-- intro panel -->
  <div class="panel" style="left:0">
    <h1 class="h-title abs" style="left:27px;top:28px">Welcome to Bay &amp;<span class="blue">Meadow Property</span><span class="blue">Services</span></h1>
    <p class="body-copy abs" style="left:27px;top:75px;width:170px">At Bay &amp; Meadow Property Services, we unlock the full potential of your investments with expert, white-glove service across <b class="blue">long-term rentals</b>, <b class="blue">short-term vacation rentals</b> (Nestly/Roamstay), and <b class="blue">mini-maxi storage</b>—maximizing value and returns.</p>
    <h2 class="h-title abs" style="left:27px;top:134px">Our Expertise<span class="blue">Includes</span></h2>

    <div class="item" style="left:27px;top:174px">
      <span class="item-icon"><svg viewBox="0 0 10 10"><path d="M1 6l3-3 2 2 3-3" stroke="#fff" fill="none" stroke-width="1.2"/></svg></span>
      <span class="item-pill pill-dark">Deal Sourcing</span>
      <p class="item-desc">Targeted, high-return investment opportunities.</p>
    </div>
    <div class="item" style="left:27px;top:215px">
      <span class="item-icon dark"><svg viewBox="0 0 10 10"><circle cx="4" cy="4" r="2.5" stroke="#fff" fill="none"/><path d="M6 6l3 3" stroke="#fff"/></svg></span>
      <span class="item-pill pill-blue">Project Oversight</span>
      <p class="item-desc">Efficient design, construction, and renovations</p>
    </div>
    <div class="item" style="left:27px;top:256px">
      <span class="item-icon"><svg viewBox="0 0 10 10"><rect x="2" y="1" width="6" height="8" stroke="#fff" fill="none"/><path d="M3.5 4h3M3.5 6h3" stroke="#fff"/></svg></span>
      <span class="item-pill pill-dark">Regulatory Setup</span>
      <p class="item-desc">Fast, compliant property launches.</p>
    </div>
    <div class="item" style="left:27px;top:292px">
      <span class="item-icon dark"><svg viewBox="0 0 10 10"><circle cx="5" cy="3.5" r="2" stroke="#fff" fill="none"/><path d="M1.5 9c.5-2.5 6.5-2.5 7 0" stroke="#fff" fill="none"/></svg></span>
      <span class="item-pill pill-blue">Full-Service Management</span>
      <p class="item-desc">End-to-end tenant and property operations.</p>
    </div>
    <div class="item" style="left:27px;top:333px">
      <span class="item-icon"><svg viewBox="0 0 10 10"><path d="M2 1h4l2 2v6H2z" stroke="#fff" fill="none"/></svg></span>
      <span class="item-pill pill-dark">Exit Strategy</span>
      <p class="item-desc">Profitable, well-timed asset sales.</p>
    </div>

    <div class="abs" style="left:31px;top:386px;width:79px;height:79px;border-radius:50%;background:var(--blue)"></div>
    <div class="photo photo-circle" role="img" aria-label="Two-storey grey suburban house with lawn" style="left:27px;top:386px;width:78px;height:78px;background:linear-gradient(180deg,#b9c6d2 0%,#5d6670 55%,#4f8a3a 100%)"></div>
    <div class="abs" style="left:112px;top:386px;width:79px;height:79px;border-radius:50%;background:var(--blue)"></div>
    <div class="photo photo-circle" role="img" aria-label="Modern grey family home with walkway" style="left:108px;top:386px;width:78px;height:78px;background:linear-gradient(180deg,#e4ebf0 0%,#6c7278 50%,#5d8f3d 100%)"></div>
  </div>

  <!-- why panel -->
  <div class="panel on-dark" style="left:213px;background:var(--ink)">
    <h2 class="h-title abs" style="left:25px;top:28px;color:var(--white)">Grounded in Expertise.<span class="blue">Built for Performance.</span></h2>
    <div class="abs" style="left:25px;top:68px;width:136px;height:20px;border-radius:10px;background:var(--blue);color:var(--white);font-weight:700;font-size:11px;line-height:20px;text-align:center">Why Work With Us?</div>

    <div class="why" style="top:102px"><p class="why-title"><svg viewBox="0 0 8 8"><circle cx="4" cy="4" r="4" fill="#fff"/><path d="M2 4l1.5 1.5L6 2.5" stroke="#231f20" fill="none"/></svg>Turnkey Execution:</p><p class="why-desc">We manage the entire process acquisition to exit.</p></div>
    <div class="why" style="top:136px"><p class="why-title"><svg viewBox="0 0 8 8"><circle cx="4" cy="4" r="4" fill="#fff"/><path d="M2 4l1.5 1.5L6 2.5" stroke="#231f20" fill="none"/></svg>High-Growth Focus:</p><p class="why-desc">Specialists in STRs and storage, today's top-performing asset classes.</p></div>
    <div class="why" style="top:170px"><p class="why-title"><svg viewBox="0 0 8 8"><circle cx="4" cy="4" r="4" fill="#fff"/><path d="M2 4l1.5 1.5L6 2.5" stroke="#231f20" fill="none"/></svg>Proven Results:</p><p class="why-desc">Profitable projects built and managed from scratch.</p></div>
    <div class="why" style="top:204px"><p class="why-title"><svg viewBox="0 0 8 8"><circle cx="4" cy="4" r="4" fill="#fff"/><path d="M2 4l1.5 1.5L6 2.5" stroke="#231f20" fill="none"/></svg>Automated Efficiency:</p><p class="why-desc">Tech-driven systems optimize revenue and operations.</p></div>
    <div class="why" style="top:238px"><p class="why-title"><svg viewBox="0 0 8 8"><circle cx="4" cy="4" r="4" fill="#fff"/><path d="M2 4l1.5 1.5L6 2.5" stroke="#231f20" fill="none"/></svg>Investor-Aligned:</p><p class="why-desc">Hands-on or hands-off—we support your preferred approach.</p></div>

    <div class="dots abs" style="left:0;width:213px;top:281px;color:var(--white)"><i></i><i></i><i></i><i></i><i></i><i></i></div>

    <div class="brand abs" style="left:52px;top:304px">
      <span class="brand-dot"></span>
      <span class="brand-name" style="color:var(--white)">Bay &amp; Meadow<br>Property Services</span>
    </div>

    <p class="abs" style="left:0;width:213px;top:352px;text-align:center;color:var(--blue);font-weight:700;font-size:12px;line-height:14px">CONTACT</p>
    <div class="abs" style="left:72px;top:368px;width:70px;height:1px;background:var(--blue)"></div>

    <svg class="abs" style="left:100px;top:377px" width="13" height="13" viewBox="0 0 13 13"><circle cx="6.5" cy="6.5" r="6.5" fill="#09a3cb"/><path d="M4.3 3.5c-.6.5-.4 2 1 3.5s3 1.7 3.5 1l.5-.7-1.2-.9-.6.5c-.5-.2-1.4-1.1-1.6-1.6l.5-.6-.9-1.2z" fill="#fff"/></svg>
    <p class="abs" style="left:0;width:213px;top:397px;text-align:center;color:var(--white);font-weight:600;font-size:6.5px">(555) 214-0387</p>

    <svg class="abs" style="left:100px;top:411px" width="13" height="13" viewBox="0 0 13 13"><circle cx="6.5" cy="6.5" r="6.5" fill="#09a3cb"/><rect x="3.5" y="4.5" width="6" height="4" stroke="#fff" fill="none" stroke-width=".8"/><path d="M3.5 4.5l3 2.2 3-2.2" stroke="#fff" fill="none" stroke-width=".8"/></svg>
    <p class="abs" style="left:0;width:213px;top:428px;text-align:center;color:var(--white);font-size:6.3px">info@bayandmeadowproperty.com</p>

    <svg class="abs" style="left:100px;top:441px" width="13" height="13" viewBox="0 0 13 13"><circle cx="6.5" cy="6.5" r="6.5" fill="#09a3cb"/><circle cx="6.5" cy="6.5" r="3.3" stroke="#fff" fill="none" stroke-width=".8"/><ellipse cx="6.5" cy="6.5" rx="1.4" ry="3.3" stroke="#fff" fill="none" stroke-width=".7"/><path d="M3.2 6.5h6.6" stroke="#fff" stroke-width=".7"/></svg>
    <p class="abs" style="left:0;width:213px;top:459px;text-align:center;color:var(--white);font-size:6.3px">halvernq7.example-host.com</p>
  </div>

  <!-- cover panel -->
  <div class="panel" style="left:426px">
    <div class="abs" style="left:0;top:246px;width:212px;height:247px;background:var(--blue)"></div>
    <div class="brand abs" style="left:42px;top:32px">
      <span class="brand-dot" style="width:30px;height:30px"></span>
      <span class="brand-name" style="color:var(--ink);font-size:11px;line-height:13px">Bay &amp; Meadow<br>Property Services</span>
    </div>
    <div class="abs" style="left:18px;top:100px;width:184px;height:184px;border-radius:50%;background:var(--ink)"></div>
    <div class="photo photo-circle" role="img" aria-label="White craftsman-style house with front lawn and young tree" style="left:16px;top:112px;width:160px;height:160px;border:3px solid var(--white);background:linear-gradient(180deg,#dfe6ec 0%,#c9ced3 45%,#eceae6 62%,#6ea13e 80%,#4e8a2e 100%)"></div>

    <p class="abs" style="left:0;width:212px;top:293px;text-align:center;font-weight:800;font-size:17px;line-height:17px;color:var(--white)">Maximize Value.<br><span style="color:var(--ink)">Maximize Returns.</span></p>
    <div class="dots abs" style="left:0;width:212px;top:339px;color:var(--white)"><i></i><i></i><i></i><i></i><i></i><i></i></div>
    <p class="abs" style="left:0;width:212px;top:347px;text-align:center;font-family:'Great Vibes',cursive;font-size:18px;color:var(--white)">Welcome to the</p>
    <p class="abs" style="left:0;width:212px;top:370px;text-align:center;font-family:'Libre Baskerville',serif;font-size:11px;color:var(--ink)">Bay &amp; Meadow Difference</p>

    <div class="abs" style="left:71px;top:396px;width:1px;height:42px;border-left:1px dashed var(--white)"></div>
    <div class="abs" style="left:126px;top:396px;width:1px;height:42px;border-left:1px dashed var(--white)"></div>

    <div class="abs" style="left:34px;top:402px;width:22px;height:22px;border-radius:50%;background:var(--ink);display:flex;align-items:center;justify-content:center"><svg width="12" height="12" viewBox="0 0 12 12"><path d="M2 6l4-4 4 4v4H2z" stroke="#fff" fill="none"/></svg></div>
    <p class="abs" style="left:20px;width:50px;top:426px;text-align:center;color:var(--white);font-size:7px;line-height:8px">Residential Rental</p>

    <div class="abs" style="left:87px;top:402px;width:22px;height:22px;border-radius:50%;background:var(--ink);display:flex;align-items:center;justify-content:center"><svg width="12" height="12" viewBox="0 0 12 12"><rect x="2" y="3" width="8" height="7" stroke="#fff" fill="none"/><circle cx="4" cy="2.5" r="1.5" stroke="#fff" fill="none"/></svg></div>
    <p class="abs" style="left:73px;width:50px;top:426px;text-align:center;color:var(--white);font-size:7px;line-height:8px">Short-term Rentals</p>

    <div class="abs" style="left:147px;top:402px;width:22px;height:22px;border-radius:50%;background:var(--ink);display:flex;align-items:center;justify-content:center"><svg width="12" height="12" viewBox="0 0 12 12"><path d="M1.5 5L6 2l4.5 3v5h-9z" stroke="#fff" fill="none"/><path d="M3.5 6h5M3.5 8h5" stroke="#fff"/></svg></div>
    <p class="abs" style="left:126px;width:66px;top:427px;text-align:center;color:var(--white);font-size:7px;line-height:8px">Mini/Maxi Storage Rental</p>

    <div class="abs" style="left:26px;top:453px;width:159px;height:12px;border-radius:6px;background:var(--ink);color:var(--white);font-size:6.8px;font-weight:600;letter-spacing:.6px;line-height:12px;text-align:center">www.<span class="blue">halvernq7.example-host</span>.com</div>
  </div>
</section>

<!-- INSIDE SHEET -->
<section class="sheet sheet-inside">
  <div class="abs" style="left:0;top:237px;width:638px;height:256px;background:var(--ink)"></div>

  <!-- residential -->
  <div class="panel on-dark" style="left:0">
    <div class="photo" role="img" aria-label="Aerial view of a leafy suburban neighbourhood" style="left:24px;top:0;width:163px;height:110px;border:2px solid var(--blue);border-top:0;border-radius:0 0 14px 14px;background:linear-gradient(160deg,#5f8d3b 0%,#8a9a70 40%,#4d7a33 70%,#7d8a66 100%)"></div>
    <h2 class="h-title abs" style="left:27px;top:124px">Residential Rental<span class="blue">Real Estate Sector</span></h2>
    <p class="body-copy abs" style="left:27px;top:152px;width:158px;color:var(--ink)">The residential rental sector offers steady demand, income potential, and portfolio diversification for investors. Tenants seek flexible, connected living spaces, while rental managers play a key role in maximizing returns through efficient operations and service innovation—adapting to evolving lifestyle trends, tech needs, and economic shifts in both urban and suburban markets.</p>

    <p class="abs" style="left:27px;top:253px;font-weight:700;font-size:9.5px;color:var(--white)">Our Services <span class="blue">Include</span></p>
    <div class="item" style="left:27px;top:275px"><span class="item-icon"><svg viewBox="0 0 10 10"><path d="M2 8V5M5 8V2M8 8V4" stroke="#fff" stroke-width="1.3"/></svg></span><span class="item-pill pill-light">Market Analysis</span><p class="item-desc">Data-driven insights on trends, demand, and ROI.</p></div>
    <div class="item" style="left:27px;top:316px"><span class="item-icon" style="background:#fff"><svg viewBox="0 0 10 10"><circle cx="4" cy="4" r="2.5" stroke="#09a3cb" fill="none"/><path d="M6 6l3 3" stroke="#09a3cb"/></svg></span><span class="item-pill pill-blue">Off-Market Sourcing</span><p class="item-desc">Access to exclusive, high-potential properties.</p></div>
    <div class="item" style="left:27px;top:357px"><span class="item-icon"><svg viewBox="0 0 10 10"><circle cx="3" cy="6" r="1.6" stroke="#fff" fill="none"/><circle cx="7" cy="6" r="1.6" stroke="#fff" fill="none"/><circle cx="5" cy="2.5" r="1.4" stroke="#fff" fill="none"/></svg></span><span class="item-pill pill-light">Investment Matching</span><p class="item-desc">Customized opportunities aligned with your goals.</p></div>
    <div class="item" style="left:27px;top:393px"><span class="item-icon" style="background:#fff"><svg viewBox="0 0 10 10"><circle cx="4" cy="4" r="2.5" stroke="#09a3cb" fill="none"/><path d="M6 6l3 3" stroke="#09a3cb"/></svg></span><span class="item-pill pill-blue">Due Diligence</span><p class="item-desc">Full vetting of zoning, title, and site conditions.</p></div>
    <div class="item" style="left:27px;top:434px"><span class="item-icon"><svg viewBox="0 0 10 10"><path d="M2 9V4l3-2 3 2v5z" stroke="#fff" fill="none"/></svg></span><span class="item-pill pill-light">Redevelopment Scouting</span><p class="item-desc">Identifying value-add and conversion potential.</p></div>
  </div>

  <!-- short-term -->
  <div class="panel on-dark" style="left:213px">
    <div class="abs" style="left:0;top:0;width:211px;height:237px;background:var(--blue)"></div>
    <div class="photo" role="img" aria-label="Hands reviewing paperwork beside a small model house and calculator" style="left:24px;top:-82px;width:164px;height:164px;border-radius:50%;border:2px solid var(--white);background:linear-gradient(180deg,#d8d5d0 0%,#efeeec 55%,#b8b2aa 100%)"></div>
    <h2 class="h-title abs" style="left:24px;top:101px">Short-Term Rental<span style="display:block;color:var(--white)">Real Estate Sector</span></h2>
    <p class="body-copy abs" style="left:24px;top:128px;width:178px;color:var(--white)">The short-term rental sector offers high income potential and flexibility, driven by platforms like Nestly and Roamstay. Demand is fueled by travel trends, staycations, and remote work. Success requires dynamic pricing, regulatory compliance, and adaptability to market shifts, making informed, strategic management key to maximizing returns.</p>

    <div class="abs" style="left:24px;top:197px;width:77px;height:81px;border-radius:50%;background:var(--blue)"></div>
    <div class="photo photo-circle" role="img" aria-label="Hands exchanging house keys over a signed document" style="left:24px;top:197px;width:77px;height:77px;border:1px solid var(--white);background:linear-gradient(135deg,#3a3230 0%,#8c7a6c 60%,#d9d2c9 100%)"></div>
    <div class="abs" style="left:108px;top:197px;width:77px;height:81px;border-radius:50%;background:var(--blue)"></div>
    <div class="photo photo-circle" role="img" aria-label="Bright hotel-style bedroom with white bedding" style="left:108px;top:197px;width:77px;height:77px;border:1px solid var(--white);background:linear-gradient(180deg,#e9e8e6 0%,#d6d2cc 55%,#a89888 100%)"></div>

    <p class="abs" style="left:26px;top:291px;font-weight:700;font-size:9.5px;color:var(--white)">Our Services <span class="blue">Include</span></p>
    <div class="item" style="left:26px;top:313px"><span class="item-icon"><svg viewBox="0 0 10 10"><circle cx="5" cy="5" r="3" stroke="#fff" fill="none"/><circle cx="5" cy="5" r="1" fill="#fff"/></svg></span><span class="item-pill pill-light">STR Opportunity Sourcing</span><p class="item-desc">Exclusive access to high-potential, STR-ready properties.</p></div>
    <div class="item" style="left:26px;top:354px"><span class="item-icon" style="background:#fff"><svg viewBox="0 0 10 10"><path d="M2 8V5M5 8V2M8 8V4" stroke="#09a3cb" stroke-width="1.3"/></svg></span><span class="item-pill pill-blue">ROI &amp; Occupancy Forecasting</span><p class="item-desc">Data-driven yield and booking performance projections.</p></div>
    <div class="item" style="left:26px;top:395px"><span class="item-icon"><svg viewBox="0 0 10 10"><rect x="2" y="2" width="6" height="6" stroke="#fff" fill="none"/><path d="M2 5h6" stroke="#fff"/></svg></span><span class="item-pill pill-light">Off-Market Acquisition</span><p class="item-desc">Targeted finds with zoning and traveler appeal.</p></div>
    <div class="item" style="left:26px;top:435px"><span class="item-icon" style="background:#fff"><svg viewBox="0 0 10 10"><circle cx="5" cy="5" r="3.5" stroke="#09a3cb" fill="none"/><circle cx="5" cy="5" r="1.5" stroke="#09a3cb" fill="none"/></svg></span><span class="item-pill pill-blue">Market Positioning</span><p class="item-desc">Strategic listing optimization to attract and convert ideal guests.</p></div>
  </div>

  <!-- storage -->
  <div class="panel on-dark" style="left:426px">
    <div class="photo" role="img" aria-label="Aerial view of long rows of self-storage buildings" style="left:20px;top:0;width:163px;height:110px;border:2px solid var(--blue);border-top:0;border-radius:0 0 14px 14px;background:linear-gradient(180deg,#c9ced3 0%,#7c8a60 30%,#6f8b95 55%,#3d5560 80%,#6f8050 100%)"></div>
    <h2 class="h-title abs" style="left:20px;top:124px">Mini &amp; Maxi Storage<span class="blue">Real Estate Sector</span></h2>
    <p class="body-copy abs" style="left:20px;top:152px;width:160px;color:var(--ink)">Mini and maxi storage facilities offer flexible, in-demand solutions for personal and business needs. With steady demand, economic resilience, and strong cash flow potential, this sector provides investors with stable, long-term returns. Blending accessibility and profitability, storage real estate appeals to those seeking diversified, tangible, and income-generating assets.</p>

    <p class="abs" style="left:20px;top:253px;font-weight:700;font-size:9.5px;color:var(--white)">Our Services <span class="blue">Include</span></p>
    <div class="item" style="left:20px;top:275px"><span class="item-icon"><svg viewBox="0 0 10 10"><rect x="1.5" y="2" width="7" height="6" stroke="#fff" fill="none"/><path d="M4 2v6M1.5 5h7" stroke="#fff"/></svg></span><span class="item-pill pill-light">Layout Optimization</span><p class="item-desc">Efficient unit sizing, traffic flow, and access controls.</p></div>
    <div class="item" style="left:20px;top:316px"><span class="item-icon" style="background:#fff"><svg viewBox="0 0 10 10"><rect x="1.5" y="2" width="7" height="6" stroke="#09a3cb" fill="none"/><path d="M3 6l2-2 2 2" stroke="#09a3cb" fill="none"/></svg></span><span class="item-pill pill-blue">Branded Design</span><p class="item-desc">Consistent, professional facility aesthetics.</p></div>
    <div class="item" style="left:20px;top:357px"><span class="item-icon"><svg viewBox="0 0 10 10"><path d="M5 1l3.5 1.5V5c0 2-1.5 3.5-3.5 4C3 8.5 1.5 7 1.5 5V2.5z" stroke="#fff" fill="none"/></svg></span><span class="item-pill pill-light">Security &amp; Environment</span><p class="item-desc">Tailored climate control, lighting, and surveillance.</p></div>
    <div class="item" style="left:20px;top:393px"><span class="item-icon" style="background:#fff"><svg viewBox="0 0 10 10"><rect x="2" y="1" width="6" height="8" stroke="#09a3cb" fill="none"/><path d="M3.5 5l1 1 2-2" stroke="#09a3cb" fill="none"/></svg></span><span class="item-pill pill-blue">Compliance</span><p class="item-desc">ADA and code-ready plans.</p></div>
    <div class="item" style="left:20px;top:424px"><span class="item-icon"><svg viewBox="0 0 10 10"><circle cx="3" cy="6" r="1.6" stroke="#fff" fill="none"/><circle cx="7" cy="6" r="1.6" stroke="#fff" fill="none"/><circle cx="5" cy="2.5" r="1.4" stroke="#fff" fill="none"/></svg></span><span class="item-pill pill-light">Vendor Management</span><p class="item-desc">Coordination with architects and engineers.</p></div>
  </div>
</section>

</body>
</html>
```